Willowbend Pharmacy Business Cards

I need a business card design and or template. Needs to convey a softer feel along with health and wellness. Please see attached logo and color scheme.

Industry/Entity Type

Pharmacy

Colors

Designer to choose colors to be used in the design.

Requirements
Must have
• I've added a second NEW colored logo I think I am going to go with the blue green logo.
• Needs to have the colors and feel of the logo attached.
• Dorian Kessel
• Pharmacy Manager
• willowbendpharmacy.example

```html
<!DOCTYPE html>
<html lang="en">
<head>
<meta charset="utf-8">
<title>Willowbend Pharmacy Business Cards</title>
<link rel="stylesheet" href="https://fonts.googleapis.com/css2?family=Vollkorn:wght@400;700&family=Arimo:wght@400&display=swap">
<style>
  :root {
    --backdrop: #e9e5df;
    --card-black: #0c0d0e;
    --card-black-soft: #1c1e20;
    --slate: #646b70;
    --leaf: #8cc63f;
    --leaf-soft: #76bb5f;
    --teal: #4fb3a4;
    --sky: #3a9fd4;
    --ink: #0b0b0b;
    --brand-grey: #8e9397;
    --paper-white: #f4f6f5;
  }
  * { margin: 0; padding: 0; box-sizing: border-box; }
  html, body { width: 1200px; height: 800px; overflow: hidden; }
  body { background: var(--backdrop); position: relative; }

  .card {
    position: absolute;
    width: 560px;
    height: 317px;
    border-radius: 3px;
    overflow: hidden;
    box-shadow: 0 6px 18px rgba(0,0,0,0.18);
  }

  /* Front card */
  .card-front {
    left: 470px;
    top: 60px;
    background: radial-gradient(ellipse at 40% 30%, var(--card-black-soft), var(--card-black) 70%);
    display: flex;
    align-items: center;
    justify-content: center;
    gap: 18px;
    padding: 0 32px;
  }
  .front-mark {
    width: 36px;
    height: 36px;
    border-radius: 50%;
    background: var(--leaf);
    flex: none;
  }
  .front-name {
    font-family: "Vollkorn", serif;
    font-weight: 700;
    font-size: 36px;
    color: var(--brand-grey);
    white-space: nowrap;
  }

  /* Back card */
  .card-back {
    left: 190px;
    top: 420px;
  }
  .back-art {
    position: absolute;
    inset: 0;
    background: linear-gradient(100deg, var(--slate) 0%, var(--slate) 30%, var(--leaf-soft) 48%, var(--teal) 72%, var(--sky) 100%);
  }
  .back-brand {
    position: absolute;
    left: 26px;
    top: 118px;
    width: 150px;
    font-family: "Vollkorn", serif;
    font-weight: 700;
    font-size: 24px;
    line-height: 1.15;
    color: var(--paper-white);
  }
  .contact {
    position: absolute;
    right: 30px;
    top: 52px;
    text-align: right;
    color: var(--ink);
  }
  .contact-name {
    font-family: "Vollkorn", serif;
    font-weight: 700;
    font-size: 39px;
    line-height: 1.1;
    letter-spacing: 0.3px;
  }
  .contact-role {
    font-family: "Vollkorn", serif;
    font-weight: 400;
    font-size: 24px;
    line-height: 1.3;
  }
  .contact-web {
    font-family: "Arimo", sans-serif;
    font-size: 19px;
    margin-top: 18px;
  }
</style>
</head>
<body>

  <section class="card card-front" aria-label="Business card front">
    <span class="front-mark" aria-hidden="true"></span>
    <span class="front-name">Willowbend Pharmacy</span>
  </section>

  <section class="card card-back" aria-label="Business card back">
    <div class="back-art" role="img" aria-label="Decorative grey, green and blue wellness background artwork"></div>
    <div class="back-brand">Willowbend Pharmacy</div>
    <div class="contact">
      <div class="contact-name">Dorian Kessel</div>
      <div class="contact-role">Pharmacy Manager</div>
      <div class="contact-web">willowbendpharmacy.example</div>
    </div>
  </section>

</body>
</html>
```